New Website design for VelvetCrate.com - A Monthly Subscription Sexy Lingerie Biz

Look at these sites: https://www.quillrazorguild.com; http://www.parcelwardrobe.com; http://www.tinyfernpack.com; https://www.ochreladle.com; https://thegoldenradish.com; http://www.petalwickcrate.com; https://wagtote.com; https://www.marlowehush.com/coral

Industry/Entity Type

Lingerie

Coding

Coded - Design and coding required

Number of Pages Required

1 page

```html
<!DOCTYPE html>
<html lang="en">
<head>
<meta charset="utf-8">
<title>VelvetCrate – Monthly Lingerie Subscription</title>
<link rel="stylesheet" href="https://fonts.googleapis.com/css2?family=Montserrat:wght@400;500;600;700&family=Questrial&display=swap">
<style>
:root{
  --ink:#111111;
  --black:#000000;
  --white:#ffffff;
  --pink:#f5577a;
  --pink-soft:#f2d2d6;
  --peach:#f6c4a6;
  --blush:#f7d9d2;
  --line:#e6e6e6;
  --partner:#222222;
  --partner-grey:#666666;
}
*{box-sizing:border-box;margin:0;padding:0}
html,body{width:1200px;height:2812px;overflow:hidden;background:var(--white)}
body{position:relative;font-family:'Questrial',sans-serif;color:var(--ink)}
.abs{position:absolute}
.label{font-family:'Montserrat',sans-serif;font-weight:600;letter-spacing:1px}

/* top bar */
.topbar{left:0;top:0;width:1200px;height:34px;background:var(--black);display:flex;align-items:center;justify-content:center;gap:10px;color:var(--white);font-family:'Montserrat',sans-serif;font-size:9px;letter-spacing:.5px}
.topbar .field{width:116px;height:20px;border:1px solid var(--white);font-size:8px;padding:4px 10px}
.topbar .btn{width:75px;height:20px;border:1px solid var(--pink);color:var(--pink);font-weight:600;font-size:9px;padding:4px 16px}

/* header */
.brand{font-family:'Montserrat',sans-serif;font-weight:500;color:var(--pink);letter-spacing:2px}
.header-brand{left:224px;top:77px;font-size:18px}
.nav{font-family:'Montserrat',sans-serif;font-size:9px;font-weight:500;letter-spacing:1px}
.nav span{position:absolute;white-space:nowrap}
.login{left:864px;top:48px;width:51px;height:18px;border:1px solid var(--ink);font-size:9px;font-family:'Montserrat',sans-serif;text-align:center;line-height:16px}
.cart{left:934px;top:47px;font-size:11px;font-family:'Montserrat',sans-serif}

/* hero */
.hero{left:0;top:124px;width:1200px;height:500px;background:linear-gradient(90deg,#d4d4d8 0%,#e6e6e9 50%,#d8d8dc 100%)}
.hero-copy{left:460px;top:167px;width:280px;text-align:center}
.hero-copy h1{font-weight:400;font-size:31px;line-height:38px;letter-spacing:2px}
.hero-copy p{margin-top:52px;font-size:14px;line-height:19px;letter-spacing:1px}
.hero-copy .price{margin-top:46px;font-family:'Montserrat',sans-serif;font-weight:600;font-size:12px;letter-spacing:1.5px}
.cta{display:block;background:var(--black);color:var(--white);font-family:'Montserrat',sans-serif;font-weight:600;font-size:13px;letter-spacing:1px;text-align:center}
.hero-cta{left:525px;top:511px;width:150px;height:47px;line-height:47px}

/* sections */
.section-title{width:1200px;left:0;text-align:center;font-weight:400;letter-spacing:2.5px}
.steps{left:0;top:624px;width:1200px;height:445px}
.step{position:absolute;width:200px;text-align:center}
.step .badge{width:132px;height:132px;border-radius:50%;margin:0 auto;border:3px dotted var(--ink)}
.step h3{margin-top:16px;font-family:'Montserrat',sans-serif;font-size:13px;font-weight:600;letter-spacing:1px}
.step p{margin-top:20px;font-family:'Montserrat',sans-serif;font-size:9px;line-height:14.5px;letter-spacing:.4px}

.brands{left:0;top:1069px;width:1200px;height:526px;background:#f1f1f1}
.brands .model{left:330px;top:0;width:590px;height:526px;background:linear-gradient(180deg,#a8745a 0%,#8a5b45 50%,#9fd8d6 75%,#b07a5f 100%);border-radius:44% 44% 20% 20%/10% 10% 10% 10%}
.partner{color:var(--partner);font-family:'Questrial',sans-serif;white-space:nowrap}

.reviews{left:0;top:1595px;width:1200px;height:273px}
.review-avatar{width:78px;height:78px;border-radius:50%;background:var(--pink);padding:7px}
.review-avatar div{width:100%;height:100%;border-radius:50%;background:linear-gradient(180deg,#5a4538,#e3c1ae)}
.review-text{font-size:10.5px;line-height:14px;letter-spacing:.6px;color:#333}
.review-name{font-family:'Montserrat',sans-serif;font-size:10px;color:var(--pink);letter-spacing:1px}

.band{left:0;top:1868px;width:1200px;height:88px;background:var(--pink)}
.band-cta{left:524px;top:1894px;width:151px;height:45px;line-height:45px}

.subscribe-field{left:424px;top:2043px;width:193px;height:46px;border:1px solid var(--pink);border-radius:3px;padding:14px 8px;font-size:13px;color:#999;letter-spacing:1px}
.subscribe-btn{left:624px;top:2043px;width:147px;height:46px;background:var(--pink);border-radius:3px;color:var(--white);font-family:'Montserrat',sans-serif;font-weight:600;font-size:12px;letter-spacing:1.5px;text-align:center;line-height:46px}
.divider{left:0;top:2126px;width:1200px;height:1px;background:var(--line)}

.gallery{left:0;top:2251px;width:1200px;height:313px;display:flex}
.gallery div{width:300px;height:313px}

.footer{left:0;top:2564px;width:1200px;height:248px;background:var(--black);color:var(--white)}
.footer-links{font-family:'Montserrat',sans-serif;font-size:8.5px;line-height:19px;letter-spacing:.6px}
.social{width:21px;height:21px;border-radius:50%;background:var(--pink)}
</style>
</head>
<body>

<div class="abs topbar">
  <span>Sign up for our newsletter!</span>
  <span class="field">your email...</span>
  <span class="btn">Sign Up</span>
</div>

<header>
  <div class="abs brand header-brand">VELVETCRATE</div>
  <div class="abs login">Login</div>
  <div class="abs cart">
    <svg width="18" height="14" viewBox="0 0 18 14" style="vertical-align:-2px"><path d="M1 1h3l2 8h9l2-6H5" fill="none" stroke="#f0a5b6" stroke-width="1.4"/><circle cx="7" cy="12" r="1.3" fill="#f0a5b6"/><circle cx="14" cy="12" r="1.3" fill="#f0a5b6"/></svg> 0
  </div>
  <nav class="abs nav" style="left:0;top:86px;width:1200px;height:12px">
    <span style="left:439px">SUBSCRIBE</span>
    <span style="left:541px">WHAT'S INSIDE</span>
    <span style="left:661px">SHOP</span>
    <span style="left:732px">BOX RESOURCES</span>
    <span style="left:864px">ABOUT</span>
    <span style="left:941px">FAQ</span>
  </nav>
</header>

<section class="abs hero">
  <div class="abs" role="img" aria-label="Two models in red and black lingerie" style="left:90px;top:0;width:360px;height:500px;background:linear-gradient(180deg,#e6c9a2 0%,#e5b49b 40%,#c8383f 60%,#3a3a3c 80%,#e0b49a 100%);opacity:.75;border-radius:40% 40% 10% 10%/12% 12% 5% 5%"></div>
  <div class="abs" role="img" aria-label="Two models in red and pink lingerie" style="left:680px;top:0;width:420px;height:500px;background:linear-gradient(180deg,#6b4a3a 0%,#e2b79e 35%,#d63a5a 55%,#f2b8c6 75%,#e2b49c 100%);opacity:.75;border-radius:40% 40% 10% 10%/12% 12% 5% 5%"></div>
</section>
<div class="abs hero-copy">
  <h1>SUPRISE<br>YOURSELF<br>EVERY MONTH!</h1>
  <p>This is Pixelwright's version<br>of Lorem Ipsum. Proin gravida<br>nibh vel velit auctor aliquet.<br>Aenean sollicitudin, lorem</p>
  <div class="price">STARTING @ $28/MO</div>
</div>
<a class="abs cta hero-cta">GET YOUR BOX</a>

<section class="abs steps">
  <h2 class="section-title abs" style="top:46px;font-size:28px">HOW IT WORKS:</h2>
  <div class="step" style="left:236px;top:119px">
    <div class="badge" role="img" aria-label="Garter belt illustration" style="background:var(--pink-soft)"></div>
    <h3>1 &nbsp;Sign Up</h3>
    <p>This is Pixelwright's version of<br>Lorem Ipsum. Proin gravida nibh vel<br>velit auctor aliquet. Aenean<br>sollicitudin, lorem quis bibendum<br>auctor, nisi elit consequat ipsum.</p>
  </div>
  <div class="step" style="left:505px;top:117px">
    <div class="badge" role="img" aria-label="Lace panties illustration" style="background:var(--peach)"></div>
    <h3 style="margin-top:18px">2 &nbsp;What's your size?</h3>
    <p>This is Pixelwright's version of<br>Lorem Ipsum. Proin gravida nibh vel<br>velit auctor aliquet. Aenean<br>sollicitudin, lorem quis bibendum<br>auctor, nisi elit consequat ipsum.</p>
  </div>
  <div class="step" style="left:765px;top:117px">
    <div class="badge" role="img" aria-label="Mesh bra illustration" style="background:var(--blush)"></div>
    <h3 style="margin-top:18px">3 &nbsp;Enjoy!</h3>
    <p>This is Pixelwright's version of<br>Lorem Ipsum. Proin gravida nibh vel<br>velit auctor aliquet. Aenean<br>sollicitudin, lorem quis bibendum<br>auctor, nisi elit consequat ipsum.</p>
  </div>
</section>

<section class="abs brands">
  <div class="abs model" role="img" aria-label="Model in mint lace lingerie making a heart with her hands"></div>
  <div class="abs partner" style="left:276px;top:78px;font-size:40px">Lunelle</div>
  <div class="abs partner" style="left:866px;top:53px;font-size:32px;letter-spacing:8px">hushline</div>
  <div class="abs partner" style="left:186px;top:314px;font-size:26px">Dawnroom</div>
  <div class="abs partner" style="left:904px;top:284px;font-size:20px">Fern &amp; Silk</div>
  <div class="abs partner" style="left:800px;top:358px;font-size:26px;letter-spacing:3px;color:var(--partner-grey)">ORLA VANE</div>
  <div class="abs partner" style="left:344px;top:450px;font-size:26px">Tessa Moor</div>
  <div class="abs partner" style="left:836px;top:428px;font-size:24px;letter-spacing:2px;text-align:center;line-height:25px">MARLOWE<br>HUSH</div>
</section>

<section class="abs reviews">
  <h2 class="section-title abs" style="top:32px;font-size:30px">PEOPLE ARE LOVING THIS IDEA</h2>
  <svg class="abs" style="left:190px;top:143px" width="12" height="20" viewBox="0 0 12 20"><path d="M10 1L2 10l8 9" fill="none" stroke="#333" stroke-width="1.3"/></svg>
  <svg class="abs" style="left:978px;top:143px" width="12" height="20" viewBox="0 0 12 20"><path d="M2 1l8 9-8 9" fill="none" stroke="#333" stroke-width="1.3"/></svg>

  <div class="abs review-avatar" style="left:220px;top:117px"><div role="img" aria-label="Customer portrait"></div></div>
  <p class="abs review-text" style="left:316px;top:118px;width:130px">"This is Pixelwright's version of Lorem Ipsum. Proin gravida nibh vel vel."</p>
  <div class="abs review-name" style="left:363px;top:202px">Mira Solano</div>

  <div class="abs review-avatar" style="left:475px;top:117px"><div role="img" aria-label="Customer portrait"></div></div>
  <p class="abs review-text" style="left:572px;top:117px;width:140px">"This is Pixelwright's version of Lorem Ipsum. Proin gravida nibh vel velit auctor aliquet. Aenean sollicitudin, lorem"</p>
  <div class="abs review-name" style="left:635px;top:203px">June Halver</div>

  <div class="abs review-avatar" style="left:735px;top:117px"><div role="img" aria-label="Customer portrait"></div></div>
  <p class="abs review-text" style="left:828px;top:117px;width:125px">"This is Pixelwright's version of Lorem Ipsum. Proin gravida nibh vel velit auctor."</p>
  <div class="abs review-name" style="left:874px;top:202px">Kira Hollis</div>
</section>

<div class="abs band"></div>
<a class="abs cta band-cta">GET YOUR BOX</a>

<h2 class="section-title abs" style="top:1982px;font-size:23px">Subscribe For Newsletters</h2>
<div class="abs subscribe-field">Enter your email...</div>
<div class="abs subscribe-btn">SUBSCRIBE</div>
<div class="abs divider"></div>

<h2 class="section-title abs" style="top:2160px;font-size:30px;letter-spacing:3px">Snapgrid @VelvetCrate</h2>
<div class="abs gallery">
  <div role="img" aria-label="Model in blue lingerie" style="background:linear-gradient(160deg,#b9b8bc,#6c5a5a 50%,#8ea0c8 80%,#9a8f90)"></div>
  <div role="img" aria-label="Three models in white lingerie" style="background:linear-gradient(180deg,#4a3630,#d7b39a 45%,#eeeeee 75%,#c6a18b)"></div>
  <div role="img" aria-label="Model in black lingerie" style="background:linear-gradient(180deg,#2b2221,#7d6556 45%,#1c1a1c 70%,#5a4a44)"></div>
  <div role="img" aria-label="Leopard print lingerie on a leather sofa" style="background:linear-gradient(160deg,#a6a4a3,#8a5a3e 45%,#3a2c2a 75%,#4b3a3a)"></div>
</div>

<footer class="abs footer">
  <div class="abs footer-links" style="left:226px;top:82px">Search<br>Login<br>Contact us<br>Terms of Use<br>Privacy Policy</div>
  <div class="abs footer-links" style="left:343px;top:82px">Subscribe<br>Get gift<br>FAQs<br>About<br>Cart 0</div>
  <div class="abs brand" style="left:536px;top:110px;font-size:17px">VELVETCRATE</div>
  <div class="abs label" style="left:795px;top:84px;font-size:8.5px;letter-spacing:.6px">Newsletter</div>
  <div class="abs" style="left:795px;top:100px;width:105px;height:24px;background:var(--white);color:var(--ink);font-family:'Montserrat',sans-serif;font-size:8.5px;padding:6px 5px">you@mailnest.com</div>
  <div class="abs label" style="left:906px;top:100px;width:70px;height:24px;background:var(--pink);font-size:8.5px;text-align:center;line-height:24px;letter-spacing:.6px">Subscribe</div>
  <div class="abs social" style="left:795px;top:148px"></div>
  <div class="abs social" style="left:826px;top:148px"></div>
  <div class="abs social" style="left:857px;top:148px"></div>
  <div class="abs label" style="left:0;top:218px;width:1200px;text-align:center;font-size:8.5px;letter-spacing:.6px">Copyright © 2016, VelvetCrate</div>
</footer>

</body>
</html>
```